Brindle Property Management Vendor Recruiting Email

We need a digital flyer to email and post on Social media to attract new vendors to our website to apply to complete maintenance work on our clients homes. I have one flyer we had produced recently that we are un-happy with. It is attached.

The example given is what we do not want!! We do not want any of the pictures used from the existing one

Target Market(s)

Construction companies and handyman

Industry/Entity Type

Residential maintenance and repairs

Requirements
Must have
• Join our team as the header not become a vendor

```html
<!DOCTYPE html>
<html lang="en">
<head>
<meta charset="UTF-8">
<title>Brindle Property Management – Join Our Team as a Header</title>
<link href="https://fonts.googleapis.com/css2?family=League+Spartan:wght@700&family=Poppins:wght@400;500;600&display=swap" rel="stylesheet">
<style>
  :root{
    --ink:#17111f;
    --text:#1c1a22;
    --muted:#4a4452;
    --purple:#9b4fa3;
    --lilac:#d49ad9;
    --violet:#7b62b0;
    --blue:#1cb8ec;
    --icon-bg:#dcecf6;
    --blush:#faf4f9;
    --white:#ffffff;
  }
  *{margin:0;padding:0;box-sizing:border-box}
  html,body{width:927px;height:1200px;overflow:hidden;background:var(--white)}
  .flyer{position:relative;width:927px;height:1200px;overflow:hidden;background:var(--blush);font-family:"Poppins",sans-serif;color:var(--text)}
  .backdrop{position:absolute;inset:0}

  .brand{position:absolute;top:38px;left:56px;display:flex;align-items:center;gap:12px;color:var(--white);font-weight:600;font-size:17px;letter-spacing:.03em}
  .brand-dot{width:22px;height:22px;border-radius:50%;background:var(--blue);flex:none}

  .headline{position:absolute;top:108px;left:56px;font-family:"League Spartan",sans-serif;font-weight:700;font-size:78px;line-height:80px;text-transform:uppercase;color:var(--white);letter-spacing:.01em}
  .headline .accent{color:var(--lilac)}

  .benefits{position:absolute;top:330px;left:40px;width:847px;display:flex;gap:22px;list-style:none}
  .benefit{flex:1;background:var(--white);border-radius:14px;padding:26px 22px 24px;box-shadow:0 10px 28px rgba(23,17,31,.12);border-top:5px solid var(--purple);font-size:18px;line-height:27px;min-height:214px}
  .benefit:nth-child(2){border-top-color:var(--violet)}
  .benefit:nth-child(3){border-top-color:var(--blue)}
  .benefit-mark{display:block;width:34px;height:34px;margin-bottom:14px}
  .benefit strong{font-weight:600}

  .section-title{position:absolute;top:606px;left:56px;font-family:"League Spartan",sans-serif;font-weight:700;font-size:42px;line-height:48px;text-transform:uppercase;color:var(--ink)}
  .section-title .accent{color:var(--purple)}
  .section-rule{position:absolute;top:664px;left:56px;width:90px;height:5px;border-radius:3px;background:linear-gradient(90deg,var(--purple),var(--blue))}

  .requirements{position:absolute;top:704px;left:56px;width:815px;list-style:none;display:grid;grid-template-columns:1fr 1fr;column-gap:40px;row-gap:22px}
  .requirements li{display:flex;align-items:center;height:92px;background:var(--white);border-radius:12px;padding:0 18px;font-size:18px;line-height:25px;box-shadow:0 4px 14px rgba(23,17,31,.06)}
  .req-icon{width:48px;height:48px;margin-right:18px;flex:none}

  .footer{position:absolute;left:0;top:1100px;width:927px;height:100px;display:flex;align-items:center;justify-content:center;gap:70px}
  .footer-item{display:flex;align-items:center;gap:14px;color:var(--white);font-weight:500;font-size:20px}
</style>
</head>
<body>
<div class="flyer">
  <svg class="backdrop" width="927" height="1200" viewBox="0 0 927 1200" aria-hidden="true">
    <defs>
      <linearGradient id="waveGrad" x1="0" x2="1">
        <stop offset="0" stop-color="#9b4fa3"/>
        <stop offset=".55" stop-color="#7b62b0"/>
        <stop offset="1" stop-color="#1cb8ec"/>
      </linearGradient>
    </defs>
    <path d="M0 0 H927 V392 C720 440 320 360 0 416 Z" fill="url(#waveGrad)"/>
    <path d="M0 0 H927 V378 C720 424 320 344 0 400 Z" fill="var(--ink)"/>
    <rect x="0" y="1094" width="927" height="6" fill="url(#waveGrad)"/>
    <rect x="0" y="1100" width="927" height="100" fill="var(--ink)"/>
  </svg>

  <div class="brand"><span class="brand-dot"></span><span>Brindle Property Management</span></div>

  <h1 class="headline">Join our team<br><span class="accent">as a Header</span></h1>

  <ul class="benefits">
    <li class="benefit">
      <svg class="benefit-mark" viewBox="0 0 34 34"><circle cx="17" cy="17" r="17" fill="#9b4fa3"/><path d="M10 17.5 l4.5 4.5 9-9" fill="none" stroke="#fff" stroke-width="2.6" stroke-linecap="round" stroke-linejoin="round"/></svg>
      <strong>95%</strong> approval rating on all submitted estimates. Guaranteed work volume.
    </li>
    <li class="benefit">
      <svg class="benefit-mark" viewBox="0 0 34 34"><circle cx="17" cy="17" r="17" fill="#7b62b0"/><path d="M10 17.5 l4.5 4.5 9-9" fill="none" stroke="#fff" stroke-width="2.6" stroke-linecap="round" stroke-linejoin="round"/></svg>
      Material purchasing program to help vendors with <strong>low capital</strong> or no or bad credit.
    </li>
    <li class="benefit">
      <svg class="benefit-mark" viewBox="0 0 34 34"><circle cx="17" cy="17" r="17" fill="#1cb8ec"/><path d="M10 17.5 l4.5 4.5 9-9" fill="none" stroke="#fff" stroke-width="2.6" stroke-linecap="round" stroke-linejoin="round"/></svg>
      Weekly secure <strong>direct deposite</strong> with net 30 payment terms.
    </li>
  </ul>

  <h2 class="section-title">Requirements to join <span class="accent">as a Header</span></h2>
  <div class="section-rule"></div>

  <ul class="requirements">
    <li><svg class="req-icon" viewBox="0 0 44 44" fill="none" stroke="#1c1a22" stroke-width="1.4"><circle cx="22" cy="22" r="22" fill="var(--icon-bg)" stroke="none"/><rect x="12" y="10" width="20" height="24" rx="2"/><line x1="16" y1="16" x2="23" y2="16"/><line x1="16" y1="20" x2="21" y2="20"/><circle cx="25" cy="26" r="4"/><path d="M23 30 v5 l2-2 2 2 v-5"/></svg>Auto insurance</li>
    <li><svg class="req-icon" viewBox="0 0 44 44" fill="none" stroke="#1c1a22" stroke-width="1.4"><circle cx="22" cy="22" r="22" fill="var(--icon-bg)" stroke="none"/><circle cx="19" cy="15" r="5.5"/><path d="M9 34 c0-7 4-11 10-11"/><path d="M28 23 l7 3 v4 c0 4-3 6-7 7 c-4-1-7-3-7-7 v-4 z"/><path d="M25 30 l2 2 4-4"/></svg>Certificate of general liability insurance</li>
    <li><svg class="req-icon" viewBox="0 0 44 44" fill="none" stroke="#1c1a22" stroke-width="1.4"><circle cx="22" cy="22" r="22" fill="var(--icon-bg)" stroke="none"/><path d="M13 18 a9 9 0 0 1 18 0 z"/><line x1="11" y1="18" x2="33" y2="18"/><path d="M15 20 c0 5 3 8 7 8 s7-3 7-8"/><path d="M10 36 c0-5 6-8 12-8 s12 3 12 8 z"/></svg>Workman’s compensation or state issued exemption letter</li>
    <li><svg class="req-icon" viewBox="0 0 44 44" fill="none" stroke="#1c1a22" stroke-width="1.4"><circle cx="22" cy="22" r="22" fill="var(--icon-bg)" stroke="none"/><rect x="8" y="13" width="28" height="18" rx="2"/><circle cx="16" cy="20" r="3"/><path d="M11 28 c1-3 3-4 5-4 s4 1 5 4"/><line x1="25" y1="19" x2="32" y2="19"/><line x1="25" y1="23" x2="32" y2="23"/><line x1="25" y1="27" x2="30" y2="27"/></svg>Drive license or state issued ID card</li>
    <li><svg class="req-icon" viewBox="0 0 44 44" fill="none" stroke="#1c1a22" stroke-width="1.4"><circle cx="22" cy="22" r="22" fill="var(--icon-bg)" stroke="none"/><circle cx="22" cy="22" r="3.5"/><path d="M15 15 a10 10 0 0 0 0 14"/><path d="M29 15 a10 10 0 0 1 0 14"/><path d="M11 11 a16 16 0 0 0 0 22"/><path d="M33 11 a16 16 0 0 1 0 22"/></svg>Coverage area</li>
    <li><svg class="req-icon" viewBox="0 0 44 44" fill="none" stroke="#1c1a22" stroke-width="1.4"><circle cx="22" cy="22" r="22" fill="var(--icon-bg)" stroke="none"/><rect x="12" y="9" width="20" height="25" rx="2"/><line x1="16" y1="15" x2="27" y2="15"/><line x1="16" y1="19" x2="27" y2="19"/><line x1="16" y1="23" x2="22" y2="23"/><circle cx="29" cy="30" r="5" fill="#fff"/><path d="M27 30 l1.5 1.5 3-3"/></svg>Any specialty licenses</li>
  </ul>

  <div class="footer">
    <div class="footer-item">
      <svg width="32" height="32" viewBox="0 0 36 36" fill="none" stroke="#fff" stroke-width="1.8" stroke-linejoin="round"><path d="M8 4 l6 1 2 7 -4 3 c2 4 5 7 9 9 l3-4 7 2 1 6 c-1 2-3 3-5 3 C15 31 5 21 5 9 c0-2 1-4 3-5 z"/><path d="M21 5 a10 10 0 0 1 10 10"/><path d="M21 10 a5 5 0 0 1 5 5"/></svg>
      <span>555-204-7316</span>
    </div>
    <div class="footer-item">
      <svg width="34" height="34" viewBox="0 0 40 40" fill="none" stroke="#fff" stroke-width="1.8"><circle cx="20" cy="20" r="17"/><ellipse cx="20" cy="20" rx="7" ry="17"/><line x1="3" y1="20" x2="37" y2="20"/><path d="M6 11 h28 M6 29 h28"/></svg>
      <span>www.brindlepropertymgmt.com</span>
    </div>
  </div>
</div>
</body>
</html>
```